Veltrana 620 practise with the goal to have business and people Elevated by the network

We need a logo design for business cards for a company based in Australia Called BOLHarvix. We specialise in cloud tech from th full Quorvane stack. i would like it to be close to quorvane colours and we specilise in Quorvane Veltrana 620 Client Linkwork. the design should display the confidence an security of a cloud based company. the tag line of Elevated by the network in the company motto.

Target Market(s)

I am targeting small to medium business up to 250 staff. i do work for not for profit and standard business.

Industry/Entity Type

Professional Service

Contact Information for Business Card

BOLHarvix Pty Ltd
A.C.N. 47 218 906 153
PO Box 837
Marrowfield 4291
Mobile: 0400382947
Email: Desmond@BolharvixMail.com.au

Font styles to use
Sans Serif

Colors

Designer to choose colors to be used in the design.

Requirements
Must have
• as a cloud based business it needs to have the this as the main theme. the tag line of Empoweredby the cloud should show we look at empowering business to get the most out of the cloud to minimise the spend they have as the target for the business is business and not for profits who need the make the most of their spend.
• the attached pictures are to be a source of insperation and key areas
Nice to have
• Quorvane Veltrana 620 is the core product that we sell and implentent for our clients so the theme should complement the Quorvane Veltrana theme

```html
<!DOCTYPE html>
<html lang="en">
<head>
<meta charset="utf-8">
<title>BOLHarvix – Business Cards</title>
<link rel="stylesheet" href="https://fonts.googleapis.com/css2?family=Roboto:wght@300;400;500&display=swap">
<style>
  :root {
    --backdrop: #1e1e1f;
    --sky-deep: #1a9fe0;
    --sky-bright: #16b6f0;
    --paper: #ffffff;
    --navy: #2f3656;
    --azure: #2aa3e3;
    --text-on-sky: #e8f7fe;
  }
  * { margin: 0; padding: 0; box-sizing: border-box; }
  html, body {
    width: 1200px; height: 800px; overflow: hidden;
    background: var(--backdrop);
    font-family: "Roboto", sans-serif;
  }
  .canvas {
    position: relative; width: 1200px; height: 800px;
    display: flex; align-items: center; justify-content: center; gap: 40px;
  }
  .card {
    position: relative; width: 540px; height: 320px; overflow: hidden;
  }

  /* Contact side */
  .card--back {
    background: linear-gradient(135deg, var(--sky-deep) 0%, var(--sky-bright) 100%);
    color: var(--text-on-sky);
  }
  .tile-field { position: absolute; display: block; }
  .card--back .tile-field--top {
    left: 0; top: 0; width: 230px; height: 70px;
    background: radial-gradient(ellipse at 0% 0%, rgba(127,214,247,0.75) 0%, rgba(127,214,247,0) 70%);
  }
  .card--back .tile-field--side {
    right: 0; top: 225px; width: 170px; height: 80px;
    background: radial-gradient(ellipse at 100% 50%, rgba(160,228,252,0.8) 0%, rgba(160,228,252,0) 70%);
  }
  .brand { position: absolute; left: 0; right: 0; text-align: center; }
  .card--back .brand { top: 62px; }
  .brand__name {
    display: inline-flex; align-items: center; gap: 8px;
    font-weight: 500; letter-spacing: 0.5px;
  }
  .brand__dot { display: inline-block; border-radius: 50%; }
  .card--back .brand__name { font-size: 30px; color: var(--paper); }
  .card--back .brand__dot { width: 10px; height: 10px; background: var(--paper); }
  .brand__tagline { display: block; font-weight: 400; }
  .card--back .brand__tagline { font-size: 9px; margin-top: 2px; color: var(--paper); }
  .glow-rule {
    position: absolute; left: 110px; top: 122px; width: 320px; height: 14px;
    background: radial-gradient(ellipse at 50% 50%, rgba(255,255,255,0.55) 0%, rgba(255,255,255,0) 70%);
  }
  .contact {
    position: absolute; font-size: 12.5px; font-weight: 300; line-height: 1.35;
    display: flex; gap: 10px;
  }
  .contact--address { left: 60px; top: 178px; }
  .contact--phone { left: 290px; top: 158px; }
  .contact--email { left: 290px; top: 188px; }
  .contact__icon { width: 12px; height: 14px; flex: none; margin-top: 1px; }
  .contact__lines { font-style: normal; }

  /* Brand side */
  .card--front { background: var(--paper); }
  .card--front .tile-field--top {
    left: 0; top: 0; width: 240px; height: 75px;
    background: radial-gradient(ellipse at 0% 0%, rgba(126,159,208,0.85) 0%, rgba(201,220,240,0.5) 45%, rgba(255,255,255,0) 75%);
  }
  .card--front .tile-field--bottom {
    right: 0; bottom: 0; width: 250px; height: 80px;
    background: radial-gradient(ellipse at 100% 100%, rgba(126,159,208,0.85) 0%, rgba(201,220,240,0.5) 45%, rgba(255,255,255,0) 75%);
  }
  .card--front .brand { top: 118px; }
  .card--front .brand__name { font-size: 44px; color: var(--navy); }
  .card--front .brand__dot { width: 14px; height: 14px; background: var(--azure); }
  .card--front .brand__tagline { font-size: 11px; margin-top: 4px; color: var(--navy); }
</style>
</head>
<body>
<main class="canvas">

  <section class="card card--back" aria-label="Business card, contact side">
    <span class="tile-field tile-field--top" role="img" aria-label="Scattered light-blue square tiles"></span>
    <span class="tile-field tile-field--side" role="img" aria-label="Scattered light-blue square tiles"></span>

    <div class="brand">
      <span class="brand__name"><span class="brand__dot"></span>BOLHarvix</span>
      <span class="brand__tagline">Elevated by the network</span>
    </div>
    <span class="glow-rule"></span>

    <div class="contact contact--address">
      <svg class="contact__icon" viewBox="0 0 12 14" aria-hidden="true">
        <path d="M6 0C2.7 0 0.5 2.4 0.5 5.3 0.5 9 6 14 6 14s5.5-5 5.5-8.7C11.5 2.4 9.3 0 6 0zm0 7.5a2.2 2.2 0 1 1 0-4.4 2.2 2.2 0 0 1 0 4.4z" fill="#ffffff"/>
      </svg>
      <address class="contact__lines">
        BOLHarvix Pty Ltd<br>
        A.C.N. 47 218 906 153<br>
        PO Box 837<br>
        Marrowfield 4291
      </address>
    </div>

    <div class="contact contact--phone">
      <svg class="contact__icon" viewBox="0 0 12 14" aria-hidden="true">
        <path d="M2.6 1.2l1.8-.6 1.5 3-1.2 1c.6 1.6 1.7 2.9 3 3.7l1.1-1.1 2.8 1.7-.6 1.8c-.3.8-1.2 1.2-2 .9C4.9 10.4 2.2 7.2 1.6 3.3c-.1-.9.3-1.8 1-2.1z" fill="#ffffff"/>
      </svg>
      <span>0400382947</span>
    </div>

    <div class="contact contact--email">
      <svg class="contact__icon" viewBox="0 0 12 14" aria-hidden="true">
        <rect x="0.5" y="3.5" width="11" height="7.5" fill="#ffffff"/>
        <path d="M0.8 3.8L6 8l5.2-4.2" stroke="#1aa8e6" stroke-width="1" fill="none"/>
      </svg>
      <span>Desmond@BolharvixMail.com.au</span>
    </div>
  </section>

  <section class="card card--front" aria-label="Business card, brand side">
    <span class="tile-field tile-field--top" role="img" aria-label="Scattered blue square tiles"></span>
    <span class="tile-field tile-field--bottom" role="img" aria-label="Scattered blue square tiles"></span>

    <div class="brand">
      <span class="brand__name"><span class="brand__dot"></span>BOLHarvix</span>
      <span class="brand__tagline">Elevated by the network</span>
    </div>
  </section>

</main>
</body>
</html>
```